Flyer Design Project

We need a flyer design for a 1 year old domestic cleaning company based in Wiltshire, England. We provide households with high quality, hard working cleaners. We would like to see designs which use blue (the colour on the logo attatched). The final design should communicate a clean, premier and thorough service in a clear and bold way. We would like the flyer to be A5 with a single sided design. We have attached an A5 word document with the words we would like to be used in the design, what we need is for you to give it some life, colour, artwork and a professional touch. We are perfectionsists which we would like to illustrate to our customer through this flyer.
Updates

payment has been guaranteed!

Sorry..... please no pictures of females on the designs. many thanks

Target Market(s)

females with higher than average income, aged 30-50. Have families and work 9-5.

Industry/Entity Type

It Company

Requirements
Must have
• The flyer must include the logo attatched and the words in the A5 document attatched. With RELIABLE CLEANERS preferably the headline. A5 - single sided.
The Flyer must also include our introductory offer.....
First Clean FREE
Allow us to demonstrate our standards

this should be emphasised.

PLEASE NOTE: can this be added to the list of words on the flyer please:

Ironing service - one day turn around
Nice to have
• some pictures - nothing cheesey. Again, pictures should communicate our modern professional approach.

```html
<!DOCTYPE html>
<html lang="en">
<head>
<meta charset="utf-8">
<title>Brookmere Cleaners – Flyer</title>
<link href="https://fonts.googleapis.com/css2?family=Arvo:wght@400;700&family=Noto+Sans:wght@400;500&family=Noto+Serif:wght@400;700&display=swap" rel="stylesheet">
<style>
  :root {
    --wood-dark: #5a2f17;
    --wood-mid: #9a5a2c;
    --wood-light: #c98a52;
    --brand-blue: #0f6ab4;
    --brand-blue-deep: #0b4f8c;
    --sun-yellow: #fcd116;
    --sun-orange: #f6a623;
    --ring-grey: #d9d9d9;
    --ink: #111111;
    --white: #ffffff;
  }
  * { box-sizing: border-box; margin: 0; padding: 0; }
  html, body { width: 1200px; height: 839px; overflow: hidden; background: #fff; }
  .flyer { position: relative; width: 1200px; height: 839px; overflow: hidden; }
  .flyer-art { position: absolute; inset: 0; }
  .headline {
    position: absolute; font-family: "Arvo", serif; font-weight: 700;
    color: var(--brand-blue); letter-spacing: 1px;
    -webkit-text-stroke: 1.5px var(--white);
    text-shadow: 0 3px 4px rgba(0,0,0,.45);
    white-space: nowrap; line-height: 1;
  }
  .headline--main { left: 20px; top: 18px; font-size: 56px; }
  .headline--offer { left: 276px; top: 88px; font-size: 60px; }
  .offer-intro {
    position: absolute; left: 278px; top: 158px;
    font-family: "Noto Sans", sans-serif; font-size: 18px; color: var(--white);
    text-shadow: 0 1px 3px rgba(0,0,0,.7); letter-spacing: .5px;
  }
  .benefits {
    position: absolute; left: 276px; top: 190px; list-style: none;
    display: grid; grid-template-columns: 306px 280px; row-gap: 7px;
    font-family: "Noto Sans", sans-serif; font-size: 19px; color: var(--white);
    text-shadow: 0 1px 3px rgba(0,0,0,.7); letter-spacing: .4px;
  }
  .benefits li { display: flex; align-items: center; gap: 11px; }
  .benefits li::before {
    content: ""; width: 12px; height: 12px; border-radius: 50%;
    background: radial-gradient(circle at 35% 35%, #fff3a0, #c9a800 70%);
    flex: none;
  }
  .promo-badge {
    position: absolute; left: 964px; top: 103px; width: 200px;
    text-align: center; font-family: "Noto Serif", serif; color: var(--white);
    font-size: 20px; line-height: 30px; text-shadow: 0 1px 2px rgba(0,0,0,.35);
  }
  .promo-badge strong { display: block; font-weight: 700; }
  .brand {
    position: absolute; left: 42px; top: 560px; display: flex; align-items: flex-end; gap: 16px;
  }
  .brand-mark { width: 70px; height: 70px; background: var(--brand-blue); }
  .brand-name {
    font-family: "Noto Sans", sans-serif; font-weight: 500; font-size: 46px;
    color: var(--ink); line-height: 1; margin-bottom: -4px;
  }
  .brand-tagline {
    position: absolute; left: 163px; top: 680px;
    font-family: "Noto Sans", sans-serif; font-weight: 500; font-size: 26px; color: var(--ink);
  }
  .contact {
    position: absolute; top: 766px; height: 45px; border-radius: 5px;
    background: linear-gradient(var(--brand-blue), var(--brand-blue-deep));
    box-shadow: 0 3px 5px rgba(0,0,0,.35);
    color: var(--white); font-family: "Noto Serif", serif; font-size: 22px;
    display: flex; align-items: center; padding-left: 11px; white-space: nowrap;
  }
  .contact--email { left: 20px; width: 523px; }
  .contact--phone { left: 550px; width: 399px; }
</style>
</head>
<body>
<main class="flyer">
  <svg class="flyer-art" width="1200" height="839" viewBox="0 0 1200 839">
    <defs>
      <linearGradient id="floorTone" x1="0" y1="0" x2="1" y2="1">
        <stop offset="0" stop-color="var(--wood-mid)"/>
        <stop offset=".5" stop-color="var(--wood-light)"/>
        <stop offset="1" stop-color="var(--wood-dark)"/>
      </linearGradient>
      <linearGradient id="sunTone" x1="0" y1="0" x2="0" y2="1">
        <stop offset="0" stop-color="var(--sun-yellow)"/>
        <stop offset="1" stop-color="var(--sun-orange)"/>
      </linearGradient>
      <radialGradient id="burstTone" cx=".5" cy=".5" r=".5">
        <stop offset="0" stop-color="#f8a51e"/>
        <stop offset="1" stop-color="#fccc2e"/>
      </radialGradient>
      <linearGradient id="dustingTone" x1="0" y1="0" x2="1" y2="1">
        <stop offset="0" stop-color="#b3261c"/><stop offset=".6" stop-color="#6b4a36"/><stop offset="1" stop-color="#3e2a1f"/>
      </linearGradient>
      <linearGradient id="vacuumTone" x1="0" y1="0" x2="0" y2="1">
        <stop offset="0" stop-color="#e6e6e4"/><stop offset=".6" stop-color="#9a9a98"/><stop offset="1" stop-color="#5b3a26"/>
      </linearGradient>
      <linearGradient id="dishTone" x1="0" y1="0" x2="0" y2="1">
        <stop offset="0" stop-color="#c49a77"/><stop offset=".5" stop-color="#e9e4df"/><stop offset="1" stop-color="#b9b4ae"/>
      </linearGradient>
    </defs>

    <rect class="floor-photo" width="1200" height="839" fill="url(#floorTone)" role="img" aria-label="Photo of a floor polishing machine on a polished wooden floor"/>
    <polygon class="diagonal-band" points="0,177 1200,736 1200,839 0,839" fill="var(--brand-blue)"/>
    <polygon class="sun-panel" points="0,270 1200,764 1200,839 0,839" fill="url(#sunTone)"/>

    <g class="promo-burst">
      <rect x="975" y="60" width="178" height="178" fill="url(#burstTone)" transform="rotate(0 1064 149)"/>
      <rect x="975" y="60" width="178" height="178" fill="url(#burstTone)" transform="rotate(15 1064 149)"/>
      <rect x="975" y="60" width="178" height="178" fill="url(#burstTone)" transform="rotate(30 1064 149)"/>
      <rect x="975" y="60" width="178" height="178" fill="url(#burstTone)" transform="rotate(45 1064 149)"/>
      <rect x="975" y="60" width="178" height="178" fill="url(#burstTone)" transform="rotate(60 1064 149)"/>
      <rect x="975" y="60" width="178" height="178" fill="url(#burstTone)" transform="rotate(75 1064 149)"/>
      <circle cx="1064" cy="149" r="100" fill="url(#burstTone)"/>
    </g>

    <g class="photo-ring">
      <circle cx="506" cy="415" r="154" fill="var(--ring-grey)"/>
      <circle cx="506" cy="415" r="131" fill="url(#dustingTone)" role="img" aria-label="Photo of a feather duster cleaning a wooden surface"/>
    </g>
    <g class="photo-ring">
      <circle cx="816" cy="575" r="121" fill="var(--ring-grey)"/>
      <circle cx="816" cy="575" r="104" fill="url(#vacuumTone)" role="img" aria-label="Photo of a man vacuuming a living room floor"/>
    </g>
    <g class="photo-ring">
      <circle cx="1076" cy="708" r="88" fill="var(--ring-grey)"/>
      <circle cx="1076" cy="708" r="72" fill="url(#dishTone)" role="img" aria-label="Photo of a plate being washed with a sponge under a tap"/>
    </g>
  </svg>

  <h1 class="headline headline--main">Reliable Cleaners!</h1>
  <h2 class="headline headline--offer">First Clean FREE</h2>
  <p class="offer-intro">Allow us to demonstrate our standards......</p>
  <ul class="benefits">
    <li>Personalised Service</li>
    <li>Insured</li>
    <li>Constantly Thorough</li>
    <li>Regular Weekly Claims</li>
    <li>Hassel Free</li>
    <li>No Contracts</li>
  </ul>

  <p class="promo-badge"><strong>Ironing Service</strong>One Day<br>Turn Around</p>

  <div class="brand">
    <span class="brand-mark"></span>
    <span class="brand-name">Brookmere Cleaners</span>
  </div>
  <p class="brand-tagline">Premier Domestic Cleaners</p>

  <p class="contact contact--email">Email: brookmerecleaners@mailbox.co.uk</p>
  <p class="contact contact--phone">Call our hotline: 07700900417</p>
</main>
</body>
</html>
```